Flyer-Design für nachhaltige Familienberatung
Reiche Ideenvielfalt (viele sehr verschiedene Designvorschläge), prompte Umsetzung aller Änderungsideen während und nach dem Wettbewerb und dazu ein sehr freundlicher Kontakt - so macht die Zusammenarbeit wirklich Spaß! Vielen Dank dafür!
Zielgruppe
Ich bin Kleinunternehmerin und berate junge Familien (auch Schwangere, Alleinerziehende und andere Angehörige) zu den Themen Stoffwindeln, Windelfrei, Babyschlaf und bedürfnis-/bindungsorientierter Erziehung. Außerdem biete ich Paarberatung und Einzelcoaching für Mütter und - gemeinsam mit meinem Mann - für Väter an.
Der Name 'Familie MiTi' steht für Mirja und Till, mich und meinem Mann, gleichzeitig ein Wortspiel mit einer 'Hasenfamilie', auf das gern angespielt werden kann.
Weitere Informationen zum Angebot können der Internetseite www.familie-miti.example entnommen werden.
Aufgabenstellung
Das Design sollte farblich und stilistisch zum Logo passen. Naturverbundenheit/Nachhaltigkeit und Familienleben/Geborgenheit dürfen im Mittelpunkt stehen.
Mein Angebot ist vielfältig - umso wichtiger ist eine übersichtliche klare Darstellung. Der Flyer sollte junge Familien ansprechen. Er sollte hochwertig und liebevoll wirken: die Leser*innen sollten ermutigt werden, mich einfach unverbindlich anzurufen/mir zu schreiben (E-Mail, Signal, WhatsApp, Facebook-Messenger) und mehr über das Angebot zu erfahren.
Die Flyer werden vor allem in Geburtshäusern, Krankenhäusern, Familienzentren und bei Frauen-/Kinderärzt*innen und Hebammen ausliegen. Außerdem werden sie durch Kooperationspartner*innen (Still-/Trageberaterinnen, in Geburtsvorbereitungskursen) verteilt.
Die hochgeladenen Fotos dürfen, müssen aber nicht verwendet werden.

```html
<!DOCTYPE html>
<html lang="de">
<head>
<meta charset="utf-8">
<title>Familie MiTi – Flyer</title>
<link rel="stylesheet" href="https://fonts.googleapis.com/css2?family=Montserrat:wght@300;700&family=Questrial&display=swap">
<style>
  :root {
    --bg: #ececec;
    --paper: #ffffff;
    --ink: #2b2b2b;
    --orange: #f0913f;
    --green: #6aa556;
  }
  * { margin: 0; padding: 0; box-sizing: border-box; }
  html, body { width: 858px; height: 1200px; overflow: hidden; }
  body { background: var(--bg); font-family: "Questrial", sans-serif; color: var(--ink); }
  .spread { position: absolute; left: 0; top: 296px; width: 858px; height: 607px; display: flex; }
  .page { position: relative; width: 429px; height: 607px; background: var(--paper); overflow: hidden; }
  .page + .page { border-left: 1px solid #f1f1f1; }
  .emblem { position: absolute; left: 0; top: 0; width: 429px; }
  .front .emblem { height: 420px; }
  .back .emblem { height: 320px; }
  .brand-mark { position: absolute; width: 72px; height: 72px; border-radius: 50%; background: var(--paper);
    display: flex; align-items: center; justify-content: center; text-align: center;
    font-family: "Questrial", sans-serif; font-size: 10px; line-height: 1.1; color: var(--orange); }
  .heading { position: absolute; left: 0; width: 100%; text-align: center; font-weight: normal; }
  .heading .kicker { display: block; font-family: "Montserrat", sans-serif; font-weight: 300; }
  .heading .title { display: block; font-family: "Montserrat", sans-serif; font-weight: 700; letter-spacing: 0.5px; }
  .rule { position: absolute; left: 50%; width: 32px; margin-left: -16px; height: 2px; background: var(--ink); }
  .copy { position: absolute; left: 0; width: 100%; text-align: center; font-size: 10.5px; line-height: 14.4px; }
  .copy p + p { margin-top: 6px; }
  .front .kicker { font-size: 26px; line-height: 28px; }
  .front .title { font-size: 44px; line-height: 46px; }
  .back .kicker { font-size: 15px; line-height: 17px; }
  .back .title { font-size: 33px; line-height: 34px; }
  .contact { font-size: 9.5px; line-height: 15.5px; font-style: normal; }
</style>
</head>
<body>
<main class="spread">
  <section class="page front">
    <svg class="emblem" viewBox="0 0 429 420">
      <defs>
        <linearGradient id="tone-couple" x1="0" y1="0" x2="0" y2="1">
          <stop offset="0" stop-color="#7d9a5a"/><stop offset="0.6" stop-color="#5e5340"/><stop offset="1" stop-color="#6f8a4a"/>
        </linearGradient>
        <linearGradient id="tone-baby" x1="0" y1="0" x2="1" y2="1">
          <stop offset="0" stop-color="#f1dcc6"/><stop offset="1" stop-color="#d9bb98"/>
        </linearGradient>
        <linearGradient id="tone-garden" x1="0" y1="0" x2="1" y2="1">
          <stop offset="0" stop-color="#4f7a3a"/><stop offset="1" stop-color="#8aa85c"/>
        </linearGradient>
        <linearGradient id="tone-teddy" x1="0" y1="0" x2="1" y2="1">
          <stop offset="0" stop-color="#8a5a36"/><stop offset="1" stop-color="#34476e"/>
        </linearGradient>
      </defs>
      <g role="img" aria-label="Foto: Paar küsst sich auf einer Holzbank am See">
        <rect x="-56" y="-56" width="112" height="112" rx="14" fill="url(#tone-couple)" transform="translate(211 114) rotate(45)"/>
      </g>
      <g role="img" aria-label="Foto: schlafendes Neugeborenes mit Kuscheltier">
        <rect x="-56" y="-56" width="112" height="112" rx="14" fill="url(#tone-baby)" transform="translate(105 222) rotate(45)"/>
      </g>
      <g role="img" aria-label="Foto: Kleinkind mit Stoffwindel krabbelt durch eine Blumenwiese">
        <rect x="-56" y="-56" width="112" height="112" rx="14" fill="url(#tone-garden)" transform="translate(318 222) rotate(45)"/>
      </g>
      <g role="img" aria-label="Foto: Kind schläft mit großem Teddybär">
        <rect x="-56" y="-56" width="112" height="112" rx="14" fill="url(#tone-teddy)" transform="translate(211 328) rotate(45)"/>
      </g>
    </svg>
    <div class="brand-mark" style="left:175px; top:186px;">Familie<br>MiTi</div>
    <h1 class="heading" style="top:410px;">
      <span class="kicker">Beratung für</span>
      <span class="title">FAMILIEN</span>
    </h1>
    <div class="rule" style="top:491px;"></div>
    <div class="copy" style="top:507px;">
      <p>Wir möchten euch unterstützen, einen natürlichen<br>und für euch passenden Weg als Familie zu finden.<br>Ob alleinerziehend oder Regenbogenfamilie - alle<br>sind willkommen!</p>
    </div>
  </section>

  <section class="page back">
    <svg class="emblem" viewBox="0 0 429 320" aria-hidden="true">
      <rect x="-56" y="-56" width="112" height="112" rx="14" fill="var(--orange)" transform="translate(218 116) rotate(45)"/>
      <rect x="-56" y="-56" width="112" height="112" rx="14" fill="var(--green)" transform="translate(112 224) rotate(45)"/>
      <rect x="-56" y="-56" width="112" height="112" rx="14" fill="var(--green)" transform="translate(326 224) rotate(45)"/>
    </svg>
    <div class="brand-mark" style="left:183px; top:186px;">Familie<br>MiTi</div>
    <h2 class="heading" style="top:286px;">
      <span class="kicker">Unser</span>
      <span class="title">ANGEBOT</span>
    </h2>
    <div class="rule" style="top:342px;"></div>
    <div class="copy" style="top:357px;">
      <p>Stoffwindelberatung, Windelfrei-Beratung, Babyschlafcoaching,<br>Paarberatung und systemisches Einzelcoaching für Eltern</p>
      <p>Wir bieten euch Beratung und Begleitung bei unruhigen<br>Nächten mit eurem Baby, beim Wickeln mit modernen Stoffwin-<br>deln oder wenn ihr euer Baby oder Kind beim trocken bleiben<br>oder werden unterstützen möchtet. Wir sind auch für euch da,<br>wenn ihr euch als Paar neu finden möchtet oder Unterstützung<br>in eurer Rolle als Eltern(teil) benötigt. Kommt gern auf uns zu!<br>Beratungen werden auch online angeboten.</p>
    </div>
    <address class="copy contact" style="top:518px;">
      Familie MiTi &nbsp;|&nbsp; Mirja Welkert &nbsp;|&nbsp; Lindenweg 12 &nbsp;|&nbsp; 12345 Musterstadt<br>
      mirja@familie-miti.example &nbsp;|&nbsp; 0151 - 00000000 &nbsp;|&nbsp; www.familie-miti.example<br>
      fb: Familie MiTi - Einfach Familie sein &nbsp;|&nbsp; Instagram: familie_miti
    </address>
  </section>
</main>
</body>
</html>
```